Corporate consulting business needs a business card

I want a professional business card.... surprise me

Updates

Reason: i dont think 2 days is enough

Target Market(s)

Corprorate and Not for Profit firms and organisations

Industry/Entity Type

Consulting

Contact Information for Business Card

Logo
Corporate Consulting Services
On Time, On Budget, Beyond Expectation
Tovan Presfield
Director
0427 31 94 62 (Larger)
tovan@tp-advisory.com.au
www.tp-advisory.com.au
include little icons beside the contact info:

- Envelope = email
- Phone = phone
- Globe = website

Font styles to use
Serif
Sans Serif

Requirements
Must have
• Professional and clean
Nice to have
• you tell me

```html
<!DOCTYPE html>
<html lang="en">
<head>
<meta charset="utf-8">
<title>TP Advisory Services – Business Card</title>
<link rel="stylesheet" href="https://fonts.googleapis.com/css2?family=Cinzel:wght@400&family=Mulish:wght@400;700&display=swap">
<style>
  :root {
    --backdrop: #e8e3dc;
    --brown: #4d2913;
    --brown-light: #5b321a;
    --band: #0c0705;
    --paper: #f5f3f0;
    --ink: #1c1410;
    --accent: #6b3712;
    --white: #ffffff;
  }
  html, body {
    margin: 0;
    padding: 0;
    width: 1200px;
    height: 1023px;
    overflow: hidden;
    background: var(--backdrop);
  }
  .canvas {
    position: relative;
    width: 1200px;
    height: 1023px;
  }
  .card {
    position: absolute;
    top: 362px;
    width: 520px;
    height: 300px;
    border-radius: 24px;
    overflow: hidden;
    box-shadow: 0 10px 28px rgba(40, 25, 15, 0.28);
  }
  .card--front { left: 60px; }
  .card--back { left: 620px; }
  .card svg { display: block; }
  .sans { font-family: "Mulish", sans-serif; }
  .serif { font-family: "Cinzel", serif; }
  .name { font-weight: 700; font-size: 19px; fill: var(--accent); }
  .role { font-size: 12px; fill: var(--ink); }
  .contact { font-size: 11.5px; fill: var(--ink); }
  .contact--phone { font-size: 13.5px; }
  .tagline { font-size: 11px; fill: var(--ink); }
  .brand { font-size: 17px; fill: var(--white); letter-spacing: 0.5px; }
  .url { font-size: 12px; fill: var(--white); letter-spacing: 0.3px; }
</style>
</head>
<body>
<main class="canvas">

  <!-- Front: contact side -->
  <section class="card card--front" aria-label="Business card front">
    <svg width="520" height="300" viewBox="0 0 520 300">
      <defs>
        <linearGradient id="brownFade" x1="0" y1="0" x2="1" y2="1">
          <stop offset="0" stop-color="var(--brown-light)"/>
          <stop offset="1" stop-color="var(--brown)"/>
        </linearGradient>
      </defs>
      <rect class="panel-brown" width="520" height="300" fill="url(#brownFade)"/>
      <path class="wave-band" d="M286,0 H520 V300 H300 C300,262 304,232 300,214 V98 C300,62 286,44 286,0 Z" fill="var(--band)"/>
      <path class="panel-paper" d="M310,0 H520 V300 H322 C322,262 336,244 336,214 V98 C336,62 310,44 310,0 Z" fill="var(--paper)"/>

      <text class="sans name" x="346" y="46">Tovan Presfield</text>
      <text class="sans role" x="346" y="64">Director</text>
      <line class="divider" x1="346" y1="90" x2="504" y2="90" stroke="var(--accent)" stroke-width="1.6"/>

      <!-- contact icons -->
      <g class="icon icon--phone" fill="none" stroke="var(--white)" stroke-width="1.4" transform="translate(312,115)">
        <path d="M2,1 L4.5,1 L5.5,3.5 L4,4.8 C4.8,6.5 5.8,7.5 7.3,8.2 L8.6,6.7 L11,7.7 L11,10 C6,10.5 1.5,6 2,1 Z"/>
      </g>
      <g class="icon icon--mail" fill="none" stroke="var(--white)" stroke-width="1.2" transform="translate(312,134)">
        <rect x="0.5" y="0.5" width="11" height="8"/>
        <path d="M0.5,0.5 L6,5 L11.5,0.5"/>
      </g>
      <g class="icon icon--globe" fill="none" stroke="var(--white)" stroke-width="1.1" transform="translate(318,156)">
        <circle r="5.5"/>
        <ellipse rx="2.4" ry="5.5"/>
        <line x1="-5.5" y1="0" x2="5.5" y2="0"/>
      </g>

      <text class="sans contact contact--phone" x="346" y="125">0427 31 94 62</text>
      <text class="sans contact" x="346" y="143">tovan@tp-advisory.com.au</text>
      <text class="sans contact" x="346" y="161">www.tp-advisory.com.au</text>

      <text class="sans tagline" x="346" y="196">Strategic Advisory Services :</text>
      <text class="sans tagline" x="346" y="211">Clear Scope,</text>
      <text class="sans tagline" x="346" y="226">Sound Plans,</text>
      <text class="sans tagline" x="346" y="241">Lasting Results</text>

      <g class="brand-lockup">
        <circle cx="140" cy="118" r="44" fill="none" stroke="var(--white)" stroke-width="3"/>
        <text class="serif brand" x="140" y="196" text-anchor="middle">TP ADVISORY SERVICES</text>
      </g>
    </svg>
  </section>

  <!-- Back: brand side -->
  <section class="card card--back" aria-label="Business card back">
    <svg width="520" height="300" viewBox="0 0 520 300">
      <defs>
        <linearGradient id="brownFadeBack" x1="0" y1="0" x2="1" y2="1">
          <stop offset="0" stop-color="var(--brown-light)"/>
          <stop offset="1" stop-color="var(--brown)"/>
        </linearGradient>
      </defs>
      <rect class="panel-brown" width="520" height="300" fill="url(#brownFadeBack)"/>
      <path class="wave-band" d="M0,250 H130 C165,250 170,230 205,230 H520 V268 H0 Z" fill="var(--band)"/>

      <g class="brand-lockup">
        <circle cx="160" cy="100" r="48" fill="none" stroke="var(--white)" stroke-width="3"/>
        <text class="serif brand" x="160" y="182" text-anchor="middle">TP ADVISORY SERVICES</text>
      </g>

      <text class="sans url" x="496" y="254" text-anchor="end">www.tp-advisory.com.au</text>
    </svg>
  </section>

</main>
</body>
</html>
```